Kestwick Holdings AG needs web design

We need a website for a Swiss company: Kestwick Holdings AG. We offer our customers financial services such as advice and funds. We also have an interest rate calculator that we want to link to via a button on the website.

We are looking for a black and gold design. (Background: Black, Accents: Gold and White)
The design should convey security and growth. We have uploaded our logo in the attachment.
Font from the logo: Trajan Pro Regular

```html
<!DOCTYPE html>
<html lang="en">
<head>
<meta charset="utf-8">
<title>Kestwick Holdings AG</title>
<link href="https://fonts.googleapis.com/css2?family=Cinzel:wght@400;600;700&family=Source+Serif+4:wght@400&display=swap" rel="stylesheet">
<style>
:root{
  --navy:#0d2150;
  --navy-deep:#041a3f;
  --footer:#0b1a3b;
  --gold:#b08d4f;
  --gold-light:#e8cf9c;
  --paper:#eef2f6;
  --white:#ffffff;
  --ink:#1d2433;
  --muted:#6b6f78;
  --line:#d9dde3;
}
*{box-sizing:border-box;margin:0;padding:0}
html,body{width:1200px;height:3616px;overflow:hidden}
body{position:relative;background:var(--white);font-family:"Cinzel",serif;color:var(--ink)}
.abs{position:absolute}
.bg-shapes{position:absolute;left:0;top:0}
.logo{left:63px;top:40px;width:230px;color:var(--gold);font-size:22px;line-height:1.25;text-align:center;font-weight:600}
.logo-mark{display:block;width:18px;height:18px;border-radius:50%;background:var(--gold);margin:0 auto 8px}
.nav{top:52px;display:flex;gap:0}
.nav a{position:absolute;color:var(--white);font-size:13px;text-decoration:none;white-space:nowrap;letter-spacing:.5px}
.nav a.active{color:var(--gold);text-decoration:underline}
.btn-gold{display:flex;align-items:center;justify-content:center;background:linear-gradient(90deg,#c9a868,#e8cf9c 50%,#b08d4f);color:var(--navy-deep);border-radius:22px;font-size:13px;font-weight:600}
.btn-line{display:flex;align-items:center;justify-content:center;border:1.5px solid var(--gold);border-radius:22px;color:var(--gold);font-size:13px}
.hero-title{left:633px;top:205px;color:var(--white);font-size:50px;line-height:56px;font-weight:600}
.hero-sub{left:633px;top:386px;color:var(--white);font-size:16px;line-height:24px;width:460px}
.hero-btn{left:633px;top:467px;width:157px;height:38px;border:1.5px solid var(--white);border-radius:22px;color:var(--white);font-size:13px;display:flex;align-items:center;justify-content:center}
.ticker{left:222px;top:673px;font-size:14px;color:var(--gold)}
.ticker b{font-weight:600}
.rule{left:63px;width:1072px;height:1px;background:var(--line)}
.photo{border-radius:14px}
.about-title{left:554px;top:836px;font-size:31px;color:var(--gold)}
.about-text{left:554px;top:890px;width:506px;font-family:"Source Serif 4",serif;font-size:12.5px;line-height:19px;color:var(--muted)}
.about-text p+p{margin-top:18px}
.section-title{left:0;width:1200px;text-align:center;font-size:31px;color:var(--gold);letter-spacing:1px}
.card-label{height:52px;background:var(--white);border-left:5px solid var(--gold);display:flex;align-items:center;padding-left:18px;font-size:19px;color:var(--ink);box-shadow:0 6px 14px rgba(0,0,0,.08)}
.card-label.on{background:var(--gold);color:var(--white);border-left-color:#8c6d36}
.band{left:63px;top:1725px;width:1072px;height:233px;background:var(--navy-deep);border-radius:6px}
.band-title{left:0;width:1200px;top:1772px;text-align:center;color:var(--white);font-size:25px;letter-spacing:1.5px}
.product{width:330px;text-align:center}
.product h3{font-size:19px;font-weight:400;color:var(--ink)}
.product p{margin-top:12px;font-size:11px;line-height:19px;color:var(--muted);letter-spacing:.5px}
.small-label{height:46px;background:var(--white);border-left:4px solid var(--gold);display:flex;align-items:center;padding-left:18px;font-size:15px;line-height:19px;box-shadow:0 6px 14px rgba(0,0,0,.08)}
.small-label.on{background:var(--gold);color:var(--white);justify-content:center;padding-left:0;border-left:none}
.form-title{left:647px;top:2970px;font-size:20px;color:var(--gold);letter-spacing:1px}
.field{border:1px solid #d9c6a0;border-radius:18px;background:rgba(255,255,255,.5);font-size:11px;color:#b9b2a6;padding:9px 14px}
.submit{left:647px;top:3199px;width:122px;height:33px;background:var(--gold);color:var(--white);border-radius:18px;font-size:13px;display:flex;align-items:center;justify-content:center}
.footer{left:0;top:3305px;width:1200px;height:311px;background:var(--footer);color:var(--white)}
.f-head{font-size:21px;display:flex;align-items:center;gap:8px}
.f-text{font-size:11.5px;line-height:20px;letter-spacing:.5px}
.social{width:32px;height:32px;border-radius:50%;background:var(--gold)}
.f-bottom{font-size:11px;letter-spacing:.5px}
</style>
</head>
<body>

<svg class="bg-shapes" width="1200" height="3616" viewBox="0 0 1200 3616" aria-hidden="true">
  <defs>
    <linearGradient id="heroFill" x1="0" y1="0" x2="1" y2="1">
      <stop offset="0" stop-color="#0a1a3e"/>
      <stop offset=".55" stop-color="#1c3a6e"/>
      <stop offset="1" stop-color="#4d6a94"/>
    </linearGradient>
    <linearGradient id="supportFill" x1="0" y1="0" x2="1" y2="0">
      <stop offset="0" stop-color="#d8dde3"/>
      <stop offset=".45" stop-color="#eceff2"/>
      <stop offset="1" stop-color="#f6f7f8"/>
    </linearGradient>
  </defs>
  <path d="M0 0H1200V1123C1100 1160 700 1090 560 1180C470 1240 250 1265 0 1123Z" fill="#eef2f6"/>
  <path d="M0 2850C200 2700 380 2690 620 2760C820 2830 1000 2860 1200 2720V3305H0Z" fill="url(#supportFill)"/>
</svg>

<!-- hero photo area -->
<svg class="abs" style="left:0;top:0" width="1200" height="640" viewBox="0 0 1200 640" role="img" aria-label="Business people reviewing documents at a desk, tinted navy">
  <path d="M0 0H1200V477C1080 560 900 632 700 632C480 632 300 520 0 323Z" fill="url(#heroFill)"/>
</svg>

<div class="abs logo"><span class="logo-mark"></span>Kestwick Holdings AG</div>

<nav class="abs nav" style="left:0;top:52px">
  <a class="active" style="left:516px">Home</a>
  <a style="left:604px">About Us</a>
  <a style="left:719px">Services</a>
  <a style="left:827px">Contact Us</a>
</nav>
<div class="abs btn-gold" style="left:966px;top:39px;width:169px;height:41px">Job Openings</div>

<h1 class="abs hero-title">Experienced.<br>Well Disposed.<br>Proficient.</h1>
<p class="abs hero-sub">We work with you to ensure your mentoring program is set up for success</p>
<div class="abs hero-btn">Contact Us</div>

<p class="abs ticker"><b>Job Openings</b> &nbsp;|&nbsp; Lorem Ipsum is simply dummy text of the printing and typesetting industry...</p>
<div class="abs rule" style="top:728px"></div>

<!-- about -->
<div class="abs photo" style="left:140px;top:810px;width:351px;height:295px;background:linear-gradient(135deg,#d6d4cf,#a7a39c 55%,#6b6e73)" role="img" aria-label="Hands working with charts, notebook and laptop"></div>
<h2 class="abs about-title">About Us</h2>
<div class="abs about-text">
  <p>Lorem Ipsum is simply dummy text of the printing and typesetting industry.</p>
  <p>Lorem Ipsum has been the industry's standard dummy text ever since the 1500s, when an unknown printer took a galley of type and scrambled it to make a type specimen book. It has survived not only five centuries, but also the leap into electronic typesetting, remaining essentially unchanged.</p>
</div>
<div class="abs btn-line" style="left:554px;top:1034px;width:174px;height:40px">Explore More</div>

<!-- we offer -->
<h2 class="abs section-title" style="top:1310px">We Offer</h2>
<div class="abs photo" style="left:157px;top:1390px;width:427px;height:231px;border-radius:8px;background:linear-gradient(135deg,#0b2a6a,#1e4fa6 50%,#2a2e3a)" role="img" aria-label="Hands on a laptop with asset management graphics"></div>
<div class="abs card-label" style="left:173px;top:1593px;width:283px">Asset Management</div>
<div class="abs photo" style="left:616px;top:1390px;width:427px;height:231px;border-radius:8px;background:linear-gradient(135deg,#e6e8ea,#8f9aa8 55%,#2c3446)" role="img" aria-label="Advisor consulting with a couple"></div>
<div class="abs card-label on" style="left:636px;top:1593px;width:279px">Investment Advice</div>

<!-- own products -->
<div class="abs band"></div>
<h2 class="abs band-title">Own Investment Products</h2>
<svg class="abs" style="left:0;top:1840px" width="1200" height="250" viewBox="0 0 1200 250" aria-hidden="true">
  <defs>
    <linearGradient id="blob" x1="0" y1="0" x2="0" y2="1">
      <stop offset="0" stop-color="#f4e3c0"/>
      <stop offset="1" stop-color="#a9874b"/>
    </linearGradient>
  </defs>
  <g transform="translate(250 125)">
    <path d="M0-110C50-110 115-30 115 50C115 95 60 105 0 105C-60 105-115 95-115 50C-115-30-50-110 0-110Z" fill="url(#blob)"/>
    <path d="M-120 55C-130-40-40-120 20-108C80-95 130-20 105 60" fill="none" stroke="#fff" stroke-width="1"/>
    <g fill="none" stroke="#3a2a10" stroke-width="3">
      <path d="M-20-30H15L28-17V30H-20Z"/><path d="M-10-12H15M-10 0H15M-10 12H15"/>
      <circle cx="-22" cy="18" r="12"/><path d="M-28 24L-16 12"/>
    </g>
  </g>
  <g transform="translate(604 125)">
    <path d="M-60-110C20-115 120-90 115-20C110 50 50 110 0 110C-50 110-100 40-110-20C-115-70-100-108-60-110Z" fill="url(#blob)"/>
    <path d="M-120-30C-110-100-40-120 40-108C110-95 130-40 110 10" fill="none" stroke="#fff" stroke-width="1"/>
    <g fill="none" stroke="#3a2a10" stroke-width="3">
      <circle cx="0" cy="-12" r="18"/><path d="M0-24V0M-5-18H5M-5-6H5"/>
      <path d="M-35 20C-20 8-8 12 5 18H22M-35 30H10L38 10"/>
    </g>
  </g>
  <g transform="translate(957 125)">
    <path d="M0-110C50-110 115-30 115 50C115 95 60 105 0 105C-60 105-115 95-115 50C-115-30-50-110 0-110Z" fill="url(#blob)"/>
    <path d="M-120 55C-130-40-40-120 20-108C80-95 130-20 105 60" fill="none" stroke="#fff" stroke-width="1"/>
    <g fill="none" stroke="#3a2a10" stroke-width="3">
      <circle cx="0" cy="0" r="20"/><path d="M0-12V12M-6-6H6M-6 6H6"/>
      <path d="M-30-5A30 30 0 0 1 25-18M30 5A30 30 0 0 1-25 18"/>
    </g>
  </g>
</svg>
<div class="abs product" style="left:85px;top:2096px"><h3>AMC</h3><p>Lorem Ipsum is simply dummy text of the printing and typesetting industry.</p></div>
<div class="abs product" style="left:439px;top:2096px"><h3>Equity Funds</h3><p>Lorem Ipsum is simply dummy text of the printing and typesetting industry.</p></div>
<div class="abs product" style="left:792px;top:2096px"><h3>Total Return Funds</h3><p>Lorem Ipsum is simply dummy text of the printing and typesetting industry.</p></div>

<div class="abs rule" style="top:2243px"></div>

<!-- partners -->
<h2 class="abs section-title" style="top:2308px;font-size:24px;letter-spacing:2px">With Independent Partners We Offer</h2>
<div class="abs photo" style="left:63px;top:2375px;width:244px;height:243px;border-radius:8px;background:linear-gradient(160deg,#efe7d8,#b59b74 60%,#6c5a40)" role="img" aria-label="Small model house beside a laptop"></div>
<div class="abs small-label" style="left:80px;top:2592px;width:211px">Real Estate</div>
<div class="abs photo" style="left:340px;top:2375px;width:244px;height:243px;border-radius:8px;background:linear-gradient(160deg,#dfe4e6,#b88a5a 55%,#7a5230)" role="img" aria-label="Wooden blocks with pension symbols"></div>
<div class="abs small-label" style="left:357px;top:2592px;width:211px">Pensions</div>
<div class="abs photo" style="left:616px;top:2375px;width:244px;height:243px;border-radius:8px;background:linear-gradient(160deg,#5a6068,#2f3338 60%,#8a8f96)" role="img" aria-label="Hand pointing at tax icons above a laptop"></div>
<div class="abs small-label on" style="left:634px;top:2592px;width:211px">Taxes</div>
<div class="abs photo" style="left:893px;top:2375px;width:242px;height:243px;border-radius:8px;background:linear-gradient(160deg,#e6d7b8,#a98b60 60%,#3a2a1a)" role="img" aria-label="Last will document with gavel"></div>
<div class="abs small-label" style="left:910px;top:2592px;width:211px;height:52px">Wills and<br>Inheritance</div>

<!-- contact form -->
<div class="abs" style="left:40px;top:2760px;width:560px;height:545px;background:radial-gradient(ellipse at 45% 45%,rgba(170,175,182,.35),rgba(238,240,242,0) 70%)" role="img" aria-label="Faded support agent with headset"></div>
<h2 class="abs form-title">How May We Help You!</h2>
<div class="abs field" style="left:647px;top:3013px;width:196px;height:34px">Name</div>
<div class="abs field" style="left:859px;top:3013px;width:196px;height:34px">Phone</div>
<div class="abs field" style="left:647px;top:3062px;width:408px;height:34px">Email</div>
<div class="abs field" style="left:647px;top:3110px;width:408px;height:70px">Message</div>
<div class="abs submit">Submit</div>

<!-- footer -->
<footer class="abs footer">
  <div class="abs f-head" style="left:63px;top:42px">
    <svg width="12" height="16" viewBox="0 0 12 16" aria-hidden="true"><path d="M6 0A6 6 0 0 0 0 6C0 10 6 16 6 16S12 10 12 6A6 6 0 0 0 6 0Z" fill="#b08d4f"/><circle cx="6" cy="6" r="2.2" fill="#0b1a3b"/></svg>
    Kestwick Holdings AG
  </div>
  <p class="abs f-text" style="left:63px;top:82px">18 Lindenweg<br>8001 Zürich</p>
  <div class="abs" style="left:63px;top:148px;width:85px;height:32px;border:1px solid #fff;border-radius:18px;font-size:11px;display:flex;align-items:center;justify-content:center">Maps</div>

  <div class="abs f-head" style="left:460px;top:42px">
    <svg width="16" height="12" viewBox="0 0 16 12" aria-hidden="true"><rect width="16" height="12" rx="1" fill="#b08d4f"/><path d="M0 1L8 7L16 1" fill="none" stroke="#0b1a3b" stroke-width="1.4"/></svg>
    Contact Us
  </div>
  <p class="abs f-text" style="left:460px;top:82px">E-mail address:<br>info@kestwickholdings.ch</p>
  <div class="abs btn-gold" style="left:457px;top:148px;width:130px;height:32px;font-weight:400;font-size:11px;color:#fff;background:var(--gold)">Contact Us</div>

  <p class="abs" style="right:65px;top:35px;font-size:30px">(+41) 44 555 0172</p>
  <p class="abs f-text" style="right:65px;top:84px">Available 8:00am - 4:00pm</p>
  <div class="abs" style="left:977px;top:148px;display:flex;gap:10px" aria-label="Social links">
    <span class="social"></span><span class="social"></span><span class="social"></span><span class="social"></span>
  </div>

  <div class="abs" style="left:63px;top:230px;width:1072px;height:1px;background:rgba(255,255,255,.15)"></div>
  <p class="abs f-bottom" style="left:63px;top:264px">Terms of Use &nbsp; - &nbsp; Contact Us &nbsp; - &nbsp; <span style="color:var(--gold)">Privacy Policy</span></p>
  <p class="abs f-bottom" style="right:65px;top:264px">Copyright © 2022 Kestwick Holdings AG. All Right Reserved</p>
</footer>

</body>
</html>
```